corvena motor oil

I would like to inform you that our new motor oil brand corvena will be divided into three categories:
Corvena high performance Full Synthetic
0w20 ,5w30 ,0w16,5w20
with massage.
Maximum Protection, Ultimate Performance.corvena pellura
--------------------------------
corvena pellura Synthetic Blend
10w40,5w30,5w20
with massage
The perfect combination of durability and efficiency
-------------------------------
corvena olvendra transmission fluid
ATF III
with massage
proven to maximize transmission life

```html
<!DOCTYPE html>
<html lang="en">
<head>
<meta charset="utf-8">
<title>Corvena Motor Oil – Label Range</title>
<link rel="stylesheet" href="https://fonts.googleapis.com/css2?family=Montserrat:wght@600;700;800&family=Oswald:wght@500;600;700&display=swap">
<style>
  :root {
    --backdrop: #3b3b3b;
    --label-dark: #1b1b1b;
    --label-mid: #4a4a4a;
    --silver-light: #f2f2f2;
    --silver-mid: #b9b9b9;
    --silver-dark: #7a7a7a;
    --ink: #0b0b0b;
    --white: #ffffff;
    --red-bright: #e2141c;
    --red-deep: #8e0a10;
    --blue-bright: #1aa3e0;
    --blue-deep: #0a2f7c;
    --accent-yellow: #f7e21c;
    --oil-gold: #d9a514;
  }
  * { margin: 0; padding: 0; box-sizing: border-box; }
  html, body { width: 1200px; height: 803px; overflow: hidden; }
  body { background: var(--backdrop); position: relative; font-family: "Montserrat", sans-serif; }
  .label { position: absolute; display: block; box-shadow: 0 10px 30px rgba(0,0,0,.45); }
  .label--full-synthetic { left: 150px; top: 215px; width: 280px; height: 395px; }
  .label--synthetic-blend { left: 505px; top: 267px; width: 265px; height: 343px; }
  .label--transmission { left: 860px; top: 358px; width: 186px; height: 252px; }
  .brand-name { font-family: "Montserrat", sans-serif; font-weight: 800; fill: var(--white); letter-spacing: 1px; }
  .viscosity { font-family: "Oswald", sans-serif; font-weight: 700; fill: var(--ink); }
  .tagline { font-family: "Montserrat", sans-serif; font-weight: 700; fill: var(--white); }
  .range-line { font-family: "Oswald", sans-serif; font-weight: 500; font-style: italic; fill: var(--white); }
  .volume { font-family: "Oswald", sans-serif; font-weight: 600; fill: var(--white); }
  .product-title { font-family: "Montserrat", sans-serif; font-weight: 800; font-style: italic; fill: #d8d8d8; }
  .grade-text { font-family: "Montserrat", sans-serif; font-weight: 800; fill: var(--ink); }
  .claim { font-family: "Montserrat", sans-serif; font-weight: 700; fill: var(--white); }
</style>
</head>
<body>

<!-- Full synthetic, 5 L -->
<svg class="label label--full-synthetic" viewBox="0 0 280 395" xmlns="http://www.w3.org/2000/svg">
  <defs>
    <linearGradient id="fs-top" x1="0" y1="0" x2="1" y2="1">
      <stop offset="0" stop-color="#2a2a2a"/><stop offset="1" stop-color="var(--label-dark)"/>
    </linearGradient>
    <linearGradient id="fs-silver" x1="0" y1="0" x2="1" y2="0">
      <stop offset="0" stop-color="var(--silver-mid)"/><stop offset=".5" stop-color="var(--silver-light)"/><stop offset="1" stop-color="var(--silver-dark)"/>
    </linearGradient>
    <linearGradient id="fs-white" x1="0" y1="0" x2="1" y2="0">
      <stop offset="0" stop-color="#d9d9d9"/><stop offset=".4" stop-color="#ffffff"/><stop offset="1" stop-color="#e6e6e6"/>
    </linearGradient>
    <linearGradient id="fs-red" x1="0" y1="0" x2="0" y2="1">
      <stop offset="0" stop-color="var(--red-bright)"/><stop offset="1" stop-color="var(--red-deep)"/>
    </linearGradient>
  </defs>
  <rect width="280" height="395" fill="url(#fs-top)"/>
  <path d="M170,0 L280,0 L280,40 L220,110 L150,110 Z" fill="var(--label-mid)" opacity=".55"/>
  <path d="M0,150 Q120,118 280,205 L280,395 L0,395 Z" fill="url(#fs-silver)"/>
  <path d="M0,160 Q120,128 280,215 L280,395 L0,395 Z" fill="url(#fs-white)"/>
  <path d="M0,272 C70,288 160,300 220,318 C250,330 270,352 280,372 L280,395 L0,395 Z" fill="url(#fs-red)"/>
  <text class="brand-name" x="140" y="106" font-size="34" text-anchor="middle">CORVENA</text>
  <rect x="27" y="173" width="161" height="74" rx="4" fill="url(#fs-silver)"/>
  <text class="viscosity" x="32" y="242" font-size="84" textLength="150" lengthAdjust="spacingAndGlyphs">5w30</text>
  <path d="M18,248 L265,248 L260,318 L14,318 Z" fill="var(--ink)"/>
  <text class="tagline" x="32" y="269" font-size="16.5">Maximum Protection</text>
  <text class="tagline" x="28" y="288" font-size="16.5">Ultimate Performance.</text>
  <text class="tagline" x="25" y="307" font-size="16.5">Corvena pellura</text>
  <path d="M12,340 L19,360 L12,380 Z" fill="var(--accent-yellow)"/>
  <text class="range-line" x="26" y="355" font-size="18" textLength="185" lengthAdjust="spacingAndGlyphs">CORVENA HIGH PERFORMANCE</text>
  <text class="range-line" x="22" y="382" font-size="18">FULL SYNTHETIC</text>
  <text class="volume" x="228" y="386" font-size="36">5L</text>
</svg>

<!-- Synthetic blend, 4 L -->
<svg class="label label--synthetic-blend" viewBox="0 0 265 343" xmlns="http://www.w3.org/2000/svg">
  <defs>
    <linearGradient id="sb-top" x1="0" y1="0" x2="1" y2="1">
      <stop offset="0" stop-color="#2a2a2a"/><stop offset="1" stop-color="var(--label-dark)"/>
    </linearGradient>
    <linearGradient id="sb-silver" x1="0" y1="0" x2="1" y2="0">
      <stop offset="0" stop-color="var(--silver-mid)"/><stop offset=".5" stop-color="var(--silver-light)"/><stop offset="1" stop-color="var(--silver-dark)"/>
    </linearGradient>
    <linearGradient id="sb-white" x1="0" y1="0" x2="1" y2="0">
      <stop offset="0" stop-color="#d9d9d9"/><stop offset=".4" stop-color="#ffffff"/><stop offset="1" stop-color="#e6e6e6"/>
    </linearGradient>
    <linearGradient id="sb-blue" x1="1" y1="0" x2="0" y2="1">
      <stop offset="0" stop-color="var(--blue-bright)"/><stop offset="1" stop-color="var(--blue-deep)"/>
    </linearGradient>
  </defs>
  <rect width="265" height="343" fill="url(#sb-top)"/>
  <path d="M160,0 L265,0 L265,35 L210,95 L140,95 Z" fill="var(--label-mid)" opacity=".55"/>
  <path d="M0,125 Q115,100 265,175 L265,343 L0,343 Z" fill="url(#sb-silver)"/>
  <path d="M0,135 Q115,110 265,185 L265,343 L0,343 Z" fill="url(#sb-white)"/>
  <path d="M0,245 C80,258 160,268 210,280 C240,288 258,305 265,322 L265,343 L0,343 Z" fill="url(#sb-blue)"/>
  <text class="brand-name" x="136" y="92" font-size="32" text-anchor="middle">CORVENA</text>
  <rect x="22" y="152" width="158" height="68" rx="4" fill="url(#sb-silver)"/>
  <text class="viscosity" x="28" y="215" font-size="76" textLength="146" lengthAdjust="spacingAndGlyphs">5w30</text>
  <path d="M17,218 L245,218 L240,277 L13,277 Z" fill="var(--ink)"/>
  <text class="tagline" x="25" y="236" font-size="14.5" textLength="214" lengthAdjust="spacingAndGlyphs">The Perfect Combination</text>
  <text class="tagline" x="22" y="252" font-size="14.5">of Durability and</text>
  <text class="tagline" x="19" y="268" font-size="14.5">Efficiency</text>
  <path d="M11,292 L17,310 L11,328 Z" fill="var(--accent-yellow)"/>
  <text class="range-line" x="24" y="306" font-size="16">CORVENA PELLURA</text>
  <text class="range-line" x="20" y="331" font-size="16">SYNTHETIC BLEND</text>
  <text class="volume" x="200" y="335" font-size="32">4L</text>
</svg>

<!-- Transmission fluid, 1 L -->
<svg class="label label--transmission" viewBox="0 0 186 252" xmlns="http://www.w3.org/2000/svg">
  <defs>
    <linearGradient id="tf-silver" x1="0" y1="0" x2="1" y2="0">
      <stop offset="0" stop-color="#5a5a5a"/><stop offset=".5" stop-color="#d6d6d6"/><stop offset="1" stop-color="#5a5a5a"/>
    </linearGradient>
    <linearGradient id="tf-dark" x1="0" y1="0" x2="0" y2="1">
      <stop offset="0" stop-color="#2b2b2b"/><stop offset="1" stop-color="var(--label-dark)"/>
    </linearGradient>
    <linearGradient id="tf-scene" x1="0" y1="0" x2="1" y2="0">
      <stop offset="0" stop-color="var(--oil-gold)"/><stop offset=".45" stop-color="#8a8a8a"/><stop offset="1" stop-color="#3d3d3d"/>
    </linearGradient>
  </defs>
  <rect width="186" height="252" fill="url(#tf-dark)"/>
  <rect width="186" height="100" fill="url(#tf-silver)"/>
  <text class="brand-name" x="93" y="66" font-size="22" text-anchor="middle">CORVENA</text>
  <text class="product-title" x="8" y="117" font-size="11.5" textLength="168" lengthAdjust="spacingAndGlyphs">CORVENA OLVENDRA</text>
  <text class="product-title" x="8" y="132" font-size="11.5" textLength="166" lengthAdjust="spacingAndGlyphs">TRANSMISSION FLUID</text>
  <rect x="51" y="140" width="84" height="22" fill="var(--accent-yellow)"/>
  <text class="grade-text" x="93" y="157" font-size="17" text-anchor="middle">ATF III</text>
  <rect x="0" y="168" width="186" height="28" fill="var(--ink)"/>
  <text class="claim" x="7" y="180" font-size="9">PROVEN TO MAXIMIZE</text>
  <text class="claim" x="13" y="191" font-size="9">TRANSMISSION LIFE</text>
  <rect x="0" y="196" width="186" height="56" fill="url(#tf-scene)" role="img" aria-label="Golden oil splash with transmission gears and bearings"/>
  <text class="grade-text" x="8" y="241" font-size="14">1L</text>
</svg>

</body>
</html>
```